Boutique Barre Studio in Geneva

Business card for pilates and dance studio. We are a brand new studio and love our fresh image with our yellow color. This business card is meant for our founder.

```html
<!DOCTYPE html>
<html lang="en">
<head>
<meta charset="utf-8">
<title>Lumen Barre – Business Card</title>
<link rel="stylesheet" href="https://fonts.googleapis.com/css2?family=Oswald:wght@300;500&family=Poppins:wght@400&display=swap">
<style>
  :root{
    --bg:#1c1c1c;
    --card-white:#ffffff;
    --card-black:#0d0d0d;
    --yellow:#f2e98a;
    --ink:#1a1a1a;
    --rule:#9a9a9a;
  }
  *{margin:0;padding:0;box-sizing:border-box}
  html,body{width:1200px;height:1108px;overflow:hidden;background:var(--bg)}
  .canvas{position:relative;width:1200px;height:1108px}
  .card{position:absolute;top:164px;width:440px;height:780px;border-radius:26px;overflow:hidden}
  .card-front{left:100px;background:var(--card-white);text-align:center}
  .card-back{left:660px;background:var(--card-black)}

  .brand{margin-top:120px;font-family:'Oswald',sans-serif;font-weight:300;font-size:92px;line-height:1;color:var(--yellow);letter-spacing:2px}
  .brand-sub{font-family:'Oswald',sans-serif;font-weight:300;font-size:30px;color:var(--yellow);letter-spacing:10px;margin-top:6px}

  .person{margin-top:170px}
  .person-name{font-family:'Oswald',sans-serif;font-weight:500;font-size:44px;color:var(--yellow);line-height:1.1}
  .person-title{font-family:'Poppins',sans-serif;font-size:20px;color:var(--ink);margin-top:2px}

  .icon-row{display:flex;align-items:center;justify-content:center;gap:8px;margin:22px 50px 14px}
  .icon-row .rule{flex:1;height:1px;background:var(--rule)}
  .icon{width:36px;height:36px;border-radius:6px;background:var(--yellow);display:flex;align-items:center;justify-content:center}

  .contact{font-family:'Poppins',sans-serif;font-size:21px;color:var(--ink);line-height:1.4}
  .divider{height:1px;background:var(--rule);margin:18px 60px}
  .address{font-family:'Poppins',sans-serif;font-size:20px;color:var(--ink);line-height:1.4}

  .back-pattern{position:absolute;inset:0;background:linear-gradient(135deg,#050505 0%,#1b1b1b 55%,#4a4a4a 100%)}
  .back-dot{position:absolute;left:196px;top:520px;width:62px;height:62px;border-radius:50%;background:var(--yellow)}
</style>
</head>
<body>
<main class="canvas">
  <section class="card card-front" aria-label="Card front">
    <h1 class="brand">Lumen</h1>
    <div class="brand-sub">BARRE</div>

    <div class="person">
      <div class="person-name">Claire Moreau</div>
      <div class="person-title">Managing Director</div>
    </div>

    <div class="icon-row">
      <span class="rule"></span>
      <span class="icon" aria-label="Phone">
        <svg width="20" height="20" viewBox="0 0 24 24"><path d="M6.6 10.8a15 15 0 0 0 6.6 6.6l2.2-2.2c.3-.3.7-.4 1-.2 1.1.4 2.3.6 3.6.6.6 0 1 .4 1 1V20c0 .6-.4 1-1 1A17 17 0 0 1 3 4c0-.6.4-1 1-1h3.5c.6 0 1 .4 1 1 0 1.3.2 2.5.6 3.6.1.3 0 .7-.2 1z" fill="#fff"/></svg>
      </span>
      <span class="icon" aria-label="Email">
        <svg width="20" height="20" viewBox="0 0 24 24"><rect x="3" y="5" width="18" height="14" fill="none" stroke="#fff" stroke-width="2"/><path d="M3 5l9 8 9-8" fill="none" stroke="#fff" stroke-width="2"/></svg>
      </span>
      <span class="icon" aria-label="Website">
        <svg width="20" height="20" viewBox="0 0 24 24"><circle cx="12" cy="12" r="9" fill="none" stroke="#fff" stroke-width="2"/><path d="M3 12h18M12 3c3 3 3 15 0 18M12 3c-3 3-3 15 0 18" fill="none" stroke="#fff" stroke-width="1.6"/></svg>
      </span>
      <span class="rule"></span>
    </div>

    <div class="contact">
      <div>022-555 018 342</div>
      <div>hello@lumenbarre.ch</div>
      <div>www.lumenbarre.ch</div>
    </div>
    <div class="divider"></div>
    <div class="address">
      <div>18, Rue des Lilas</div>
      <div>1204, Geneva</div>
    </div>
  </section>

  <section class="card card-back" aria-label="Card back">
    <div class="back-pattern" role="img" aria-label="Repeating tonal pattern of the studio monogram in gloss black"></div>
    <span class="back-dot"></span>
  </section>
</main>
</body>
</html>
```